Business Card for Financial Asset Management Company

Now we are launching a new company based in Tokyo.
The company information is below;

Company Name: Talvane Management

Operations: Financial assets management, Proposing forming portfolio of assets, Consulting service, and advising to enhance your company's financial health

Corporate Colour: Japan Blue or Navy like below
http://staffpages.qorvenly.edu/mtavis/images/Slate/Teal-Slate-217.jpg

It's dark and deep, and will get to fit to our clients as our relationships last longer and longer.

Our images for this colour are "Japanese style" and "pride in our craftmanship" , and also "gentle".

Corporate Key Image: an order taker who is sincere, polite, but courageous

We don't have our logo yet so please feel free to put any symbol on your design.

Please do not hesitate about asking any questions.
Thank you :-)

Reason: We are still discussin on final decision. Thank you for your understanding.

```html
<!DOCTYPE html>
<html lang="en">
<head>
<meta charset="utf-8">
<title>Talvane Management – Business Card</title>
<link rel="stylesheet" href="https://fonts.googleapis.com/css2?family=Cinzel:wght@400&family=Lato:wght@400;700&display=swap">
<style>
  :root {
    --navy-deep: #15124a;
    --navy: #2c2676;
    --navy-light: #3c3a94;
    --ink: #25216b;
    --grey: #7a7a82;
    --paper: #ffffff;
    --stage: #ecebf2;
    --faint: #e4e3ee;
  }
  * { box-sizing: border-box; margin: 0; padding: 0; }
  html, body { width: 1200px; height: 1000px; overflow: hidden; }
  body {
    background: var(--stage);
    font-family: "Lato", Arial, sans-serif;
    position: relative;
  }
  .card {
    position: absolute;
    left: 250px;
    width: 700px;
    height: 400px;
    overflow: hidden;
    box-shadow: 0 8px 24px rgba(20, 18, 60, 0.18);
  }

  /* Front */
  .card-front {
    top: 90px;
    background: linear-gradient(135deg, var(--navy-light) 0%, var(--navy) 45%, var(--navy-deep) 100%);
    color: var(--paper);
    text-align: center;
  }
  .card-front .sweeps { position: absolute; inset: 0; width: 100%; height: 100%; }
  .front-mark {
    position: absolute;
    left: 50%;
    top: 58px;
    width: 96px;
    height: 96px;
    margin-left: -48px;
    border-radius: 50%;
    background: var(--paper);
  }
  .front-name {
    position: absolute;
    left: 0; right: 0;
    top: 188px;
    font-family: "Cinzel", Georgia, serif;
    font-size: 40px;
    letter-spacing: 1px;
  }
  .front-tagline {
    position: absolute;
    left: 30px; right: 30px;
    bottom: 34px;
    font-size: 15px;
    line-height: 1.45;
  }

  /* Back */
  .card-back {
    top: 510px;
    background: var(--paper);
    color: var(--grey);
  }
  .edge-stripe {
    position: absolute;
    left: 0; top: 0; bottom: 0;
    width: 10px;
    background: var(--navy);
  }
  .brand {
    position: absolute;
    left: 48px;
    top: 34px;
    display: flex;
    align-items: center;
    gap: 22px;
  }
  .brand-mark {
    width: 84px;
    height: 84px;
    border-radius: 50%;
    background: var(--navy);
  }
  .brand-name {
    font-family: "Cinzel", Georgia, serif;
    font-size: 30px;
    color: var(--ink);
  }
  .person {
    position: absolute;
    left: 52px;
    top: 150px;
  }
  .person-name {
    font-weight: 700;
    font-size: 24px;
    color: var(--ink);
    letter-spacing: 0.5px;
  }
  .person-role { font-size: 16px; margin-top: 2px; }
  .contact {
    position: absolute;
    left: 52px;
    top: 222px;
    font-size: 17px;
    line-height: 1.45;
  }
  .contact-label { font-weight: 700; color: var(--ink); }
  .address {
    position: absolute;
    left: 52px;
    top: 312px;
    font-size: 17px;
    line-height: 1.35;
  }
  .address-company { font-weight: 700; color: var(--ink); }
  .watermark {
    position: absolute;
    right: 40px;
    bottom: 40px;
    width: 180px;
    height: 180px;
    border-radius: 50%;
    background: var(--faint);
  }
</style>
</head>
<body>

<section class="card card-front">
  <svg class="sweeps" viewBox="0 0 700 400" preserveAspectRatio="none" aria-hidden="true">
    <path d="M120 0 C260 140 300 260 240 400" fill="none" stroke="#ffffff" stroke-opacity="0.08" stroke-width="2"/>
    <path d="M300 0 C380 120 520 200 700 230" fill="none" stroke="#ffffff" stroke-opacity="0.07" stroke-width="2"/>
    <path d="M0 140 C180 160 380 260 520 400" fill="none" stroke="#ffffff" stroke-opacity="0.06" stroke-width="2"/>
    <path d="M420 0 C460 160 560 300 700 360 L700 0 Z" fill="#ffffff" fill-opacity="0.04"/>
  </svg>
  <div class="front-mark"></div>
  <h1 class="front-name">Talvane Management</h1>
  <p class="front-tagline">Financial Assets Management, Proposing forming Portfolio of Assets, Consulting Service<br>and Advising to enhance your Company's Financial Health.</p>
</section>

<section class="card card-back">
  <div class="edge-stripe"></div>
  <div class="brand">
    <div class="brand-mark"></div>
    <span class="brand-name">Talvane Management</span>
  </div>
  <div class="person">
    <h2 class="person-name">HARUKI MIZUNO</h2>
    <p class="person-role">CEO</p>
  </div>
  <div class="contact">
    <p><span class="contact-label">P:</span> 111 111 111</p>
    <p><span class="contact-label">F:</span> 222 222 222</p>
    <p><span class="contact-label">E:</span> haruki@talvanemanagement.jp</p>
  </div>
  <div class="address">
    <p class="address-company">Talvane Management</p>
    <p>Kaede Tower, 3rd Floor,</p>
    <p>Minato Road, Tokyo 12345</p>
  </div>
  <div class="watermark"></div>
</section>

</body>
</html>
```